International Chino Pant Manufacturer

We need modern packaging design for men's chino. All kinds of packaging designs are welcome.

The pant is folded and packaged in a poly bag. We require a label design for the brand name Tarvo. The main label will be attached by a string on the belt loop. the size of that label will 15cm in length and 5cm wide. This is the first label the customer see's when he picks up the garment. Therefore, we require an eye catching design for that. If required it could have certain information about the chino pant on the main label such as Comfort fit, Wrinkle-resistant, machine washable, luxury fabric. But, if you feel that adding the above information spoils the design of the label then it is not a must to include the above information. On the back of the label we like to include the information that this pant was manufactured in an Ecora Summit certified green plant and hence the damage to the environment because of the plant is nill.

The second label label is attached on to the waist band and the purpose of that label is to include the size of the pant such 32x32. The size of that label is 8cm in length and 4cm in width. There is no design on the back on this label it has to be blank.

Manufacturer

```html
<!DOCTYPE html>
<html lang="en">
<head>
<meta charset="utf-8">
<title>Tarvo Chino Pant – Main Label</title>
<link rel="stylesheet" href="https://fonts.googleapis.com/css2?family=Yellowtail&family=Mrs+Saint+Delafield&family=EB+Garamond:wght@400&display=swap">
<style>
  :root {
    --brown-deep: #622218;
    --orange-brush: #f05a22;
    --orange-soft: #e9561f;
    --label-white: #ffffff;
  }
  html, body {
    margin: 0;
    padding: 0;
    overflow: hidden;
    background: var(--brown-deep);
  }
  .label {
    position: relative;
    width: 1200px;
    height: 400px;
    overflow: hidden;
    background: var(--brown-deep);
  }
  .brush-stroke {
    position: absolute;
    inset: 0;
    width: 1200px;
    height: 400px;
  }
  .brand-name {
    position: absolute;
    left: 62px;
    top: 18px;
    margin: 0;
    font-family: "Yellowtail", cursive;
    font-weight: 400;
    font-size: 250px;
    line-height: 1;
    color: var(--label-white);
    letter-spacing: 2px;
  }
  .product-name {
    position: absolute;
    left: 515px;
    top: 232px;
    margin: 0;
    font-family: "Mrs Saint Delafield", cursive;
    font-size: 104px;
    line-height: 1;
    color: var(--label-white);
  }
  .fit-type {
    position: absolute;
    right: 22px;
    top: 40px;
    height: 318px;
    margin: 0;
    writing-mode: vertical-rl;
    transform: rotate(180deg);
    font-family: "EB Garamond", serif;
    font-size: 56px;
    line-height: 1;
    color: var(--label-white);
    text-align: left;
    white-space: nowrap;
  }
</style>
</head>
<body>
  <main class="label">
    <svg class="brush-stroke" viewBox="0 0 1200 400" role="img" aria-label="Orange painted brush stroke sweeping across the label">
      <defs>
        <linearGradient id="brushTone" x1="0" y1="1" x2="1" y2="0">
          <stop offset="0" stop-color="var(--orange-soft)"/>
          <stop offset="1" stop-color="var(--orange-brush)"/>
        </linearGradient>
      </defs>
      <path fill="url(#brushTone)" d="M150 262 L330 236 L520 200 L660 150 L720 100 L900 70 L1060 50 L1200 40 L1200 400 L420 400 L360 380 L200 352 L110 330 Z"/>
    </svg>

    <h1 class="brand-name">Tarvo</h1>
    <p class="product-name">chino pant</p>
    <p class="fit-type">Comfort fit</p>
  </main>
</body>
</html>
```